Southern Ribotide Manufacturing Alliance Ecosystem

We recently published an article describing the Southern Ribotide manufacturing alliance ecosystem.
https://pagefolio.example/brindlecote-press/docs/bench_and_cell_review_jun_jul_2021/6

I would like to create a logo or graphic design to represent this initiative. We are thinking of having a graphic with a hand that holds the four sections ( Genetic Medicine, Industry, Research, University / Institutions) each represented by their own graphic in one complete picture. It will be used to represent the initiative on publications, document headers and letters. We need to keep it simple but also to clearly communicate the message.
Thanks.

Target Market(s)

Medicine, Industry, Research, University, Research Institutions and federal and local government

Requirements
Must have
• We need the graphic to represent the sections highlighted in the brief, we need some representation on research, industry/manufacturing and RNA. we need the Southern Ribotide Manufacturing Alliance (SRMA) to be clearly represented that have deep expertise in the biology, chemistry, manufacture and use of RNA medicines.

```html
<!DOCTYPE html>
<html lang="en">
<head>
<meta charset="utf-8">
<title>Southern Ribotide Manufacturing Alliance Ecosystem</title>
<link rel="stylesheet" href="https://fonts.googleapis.com/css2?family=Didact+Gothic&display=swap">
<style>
  :root {
    --bg-light: #f7f9fb;
    --bg-tint: #e6eef4;
    --navy: #2f3a52;
    --ink: #4a4a4c;
    --hand-grey: #6b6b6d;
    --hand-grey-soft: #8a8a8c;
    --research: #d8145f;
    --genetic: #1ea0dc;
    --industry: #ecd04c;
    --university: #46b995;
    --disc-hi: #ffffff;
    --disc-lo: #e4e4e6;
  }
  html, body {
    margin: 0;
    padding: 0;
    width: 1200px;
    height: 848px;
    overflow: hidden;
  }
  body {
    font-family: "Didact Gothic", "Century Gothic", sans-serif;
    color: var(--ink);
  }
  .canvas {
    position: relative;
    width: 1200px;
    height: 848px;
    background:
      radial-gradient(ellipse at 85% 20%, var(--bg-tint) 0%, rgba(230,238,244,0) 45%),
      radial-gradient(ellipse at 95% 90%, #eaf1f6 0%, rgba(234,241,246,0) 40%),
      var(--bg-light);
    overflow: hidden;
  }
  .world-network {
    position: absolute;
    left: 102px;
    top: 138px;
    width: 1001px;
    height: 575px;
    border-radius: 40% 45% 35% 40%;
    background: radial-gradient(ellipse at center, rgba(201,204,209,0.32) 0%, rgba(201,204,209,0.12) 60%, rgba(201,204,209,0) 80%);
  }
  .diagram {
    position: absolute;
    inset: 0;
  }
  .sector-disc {
    position: absolute;
    width: 172px;
    height: 172px;
    border-radius: 50%;
    background: radial-gradient(circle at 40% 35%, var(--disc-hi) 0%, #f1f1f2 55%, var(--disc-lo) 100%);
    box-shadow: 4px 6px 10px rgba(0,0,0,0.22), -1px -1px 3px rgba(255,255,255,0.9);
  }
  .sector-icon {
    position: absolute;
    border-radius: 6px;
  }
  .icon-research   { left:363px; top:228px; width:75px; height:74px; background:linear-gradient(160deg, var(--research), #e8578f); }
  .icon-genetic    { left:731px; top:224px; width:83px; height:81px; background:linear-gradient(160deg, var(--genetic), #5bbbe6); }
  .icon-industry   { left:267px; top:450px; width:67px; height:87px; background:linear-gradient(180deg, #f1dc7c, var(--industry)); }
  .icon-university { left:837px; top:451px; width:93px; height:80px; background:linear-gradient(160deg, var(--university), #74cbb0); }
  .sector-label {
    position: absolute;
    width: 200px;
    text-align: center;
    font-size: 20px;
    line-height: 22px;
    color: var(--ink);
    text-transform: uppercase;
  }
  .sector-label.small {
    font-size: 15px;
    line-height: 19px;
    letter-spacing: 0.8px;
  }
  .ecosystem-title {
    position: absolute;
    left: 436px;
    top: 431px;
    width: 300px;
    text-align: center;
    font-size: 19px;
    line-height: 24px;
    letter-spacing: 0.3px;
    text-transform: uppercase;
    color: var(--ink);
    margin: 0;
    font-weight: normal;
  }
  .ecosystem-title span { display: block; white-space: nowrap; }
  .supporting-hand {
    position: absolute;
    left: 472px;
    top: 542px;
    width: 236px;
    height: 87px;
    border-radius: 12px;
    background: linear-gradient(160deg, var(--hand-grey-soft) 0%, var(--hand-grey) 60%);
    box-shadow: 0 6px 8px rgba(0,0,0,0.12);
  }
</style>
</head>
<body>
<main class="canvas">
  <div class="world-network" role="img" aria-label="Faint world map drawn as a network of connected points"></div>

  <svg class="diagram" width="1200" height="848" viewBox="0 0 1200 848" aria-hidden="true">
    <g fill="none" stroke="var(--navy)" stroke-width="1" stroke-dasharray="3 3">
      <line x1="465" y1="368" x2="503" y2="408"/>
      <line x1="712" y1="365" x2="669" y2="407"/>
      <line x1="402" y1="518" x2="448" y2="518"/>
      <line x1="784" y1="518" x2="725" y2="518"/>
    </g>

    <path d="M448 518 A138.5 138.5 0 0 1 725 518" fill="none" stroke="#4d4d4f" stroke-width="2"/>
    <g fill="#4d4d4f">
      <circle cx="503" cy="408" r="6"/>
      <circle cx="669" cy="407" r="6"/>
      <circle cx="448" cy="518" r="6"/>
      <circle cx="725" cy="518" r="6"/>
    </g>

    <g class="ring-research" fill="none" stroke-width="3">
      <path d="M400 183 A102 102 0 0 1 502 285" stroke="var(--research)"/>
      <path d="M400 183 A102 102 0 0 0 400 387" stroke="var(--navy)"/>
      <path d="M502 285 A102 102 0 0 1 400 387" stroke="var(--navy)" stroke-width="4" stroke-dasharray="4 7"/>
    </g>
    <circle cx="400" cy="388" r="8" fill="var(--research)"/>

    <g class="ring-genetic" fill="none" stroke-width="3">
      <path d="M673 284 A102 102 0 0 1 775 182" stroke="var(--genetic)"/>
      <path d="M775 182 A102 102 0 0 1 775 386" stroke="var(--navy)"/>
      <path d="M673 284 A102 102 0 0 0 775 386" stroke="var(--navy)" stroke-width="4" stroke-dasharray="4 7"/>
    </g>
    <circle cx="777" cy="387" r="8" fill="var(--genetic)"/>

    <g class="ring-industry" fill="none" stroke-width="3">
      <path d="M194 520 A102 102 0 0 1 296 418" stroke="var(--industry)"/>
      <path d="M296 418 A102 102 0 0 1 296 622" stroke="var(--navy)"/>
      <path d="M194 520 A102 102 0 0 0 296 622" stroke="var(--navy)" stroke-width="4" stroke-dasharray="4 7"/>
    </g>
    <circle cx="299" cy="624" r="8" fill="var(--industry)"/>

    <g class="ring-university" fill="none" stroke-width="3">
      <path d="M886 418 A102 102 0 0 1 988 520" stroke="var(--university)"/>
      <path d="M886 418 A102 102 0 0 0 886 622" stroke="var(--navy)"/>
      <path d="M988 520 A102 102 0 0 1 886 622" stroke="var(--navy)" stroke-width="4" stroke-dasharray="4 7"/>
    </g>
    <circle cx="883" cy="624" r="8" fill="var(--university)"/>
  </svg>

  <div class="sector-disc" style="left:314px; top:199px;"></div>
  <div class="sector-disc" style="left:689px; top:198px;"></div>
  <div class="sector-disc" style="left:210px; top:434px;"></div>
  <div class="sector-disc" style="left:800px; top:434px;"></div>

  <div class="sector-icon icon-research" role="img" aria-label="Research pictogram: microscope beside hexagon molecule cells, magenta line art"></div>
  <div class="sector-icon icon-genetic" role="img" aria-label="Genetic medicine pictogram: DNA strand with a magnifying glass, blue line art"></div>
  <div class="sector-icon icon-industry" role="img" aria-label="Industry pictogram: factory with smoking chimneys, solid yellow"></div>
  <div class="sector-icon icon-university" role="img" aria-label="University pictogram: campus building with a flag, green line art"></div>

  <div class="sector-label" style="left:300px; top:313px;">Research</div>
  <div class="sector-label" style="left:674px; top:306px;">Genetic<br>Medicine</div>
  <div class="sector-label" style="left:196px; top:549px;">Industry</div>
  <div class="sector-label small" style="left:786px; top:541px;">University&nbsp;&nbsp;/<br>Institutions</div>

  <h1 class="ecosystem-title">
    <span>Southern</span>
    <span>Ribotide Manufacturing</span>
    <span>Alliance Ecosystem</span>
  </h1>

  <div class="supporting-hand" role="img" aria-label="Open grey hand held palm up beneath the arc, supporting the ecosystem"></div>
</main>
</body>
</html>
```